psd/html for a e wallet payment website designed

hi
i am in need of a psd / html for a whole website designed
the site is a e wallet /payment system i can i will provide a link to what type of style i am looking for but i can not stress this enough i do not want anyone replicating the website i am just providing the links to show you what kind of function and the content that is involved also, i have a srs with detailed pages you can read and refer to if need be
thanks of viewing
Vantoleaf.com
Brisklune.com
marblequivercoin.com
Qrdelivane.com

```html
<!DOCTYPE html>
<html lang="en">
<head>
<meta charset="utf-8">
<title>Pursedale — online wallet</title>
<link rel="stylesheet" href="https://fonts.googleapis.com/css2?family=Oswald:wght@300;400;500;600&family=Open+Sans:wght@300;400;600;700&family=Kalam&display=swap">
<style>
  :root{
    --teal:#00a6bf;
    --teal-bright:#1fb4cc;
    --ink:#1f1f1f;
    --panel:#2e2e2e;
    --hero-edge:#161616;
    --text-dark:#222;
    --text-light:#d8d8d8;
    --white:#fff;
    --heading:'Oswald', sans-serif;
    --body:'Open Sans', sans-serif;
    --hand:'Kalam', cursive;
  }
  *{box-sizing:border-box;margin:0;padding:0}
  html,body{width:1019px;height:1200px;overflow:hidden;background:var(--white)}
  body{position:relative;font-family:var(--body);color:var(--text-dark)}
  .abs{position:absolute}

  /* top bar */
  .topbar{left:0;top:0;width:1019px;height:36px;background:var(--ink)}
  .topbar__welcome{left:17px;top:9px;font:13px Arial, sans-serif;color:var(--white)}
  .account-tab{left:752px;top:28px;width:233px;height:18px;background:var(--ink);clip-path:polygon(0 0,100% 0,96% 100%,4% 100%)}
  .account-tab__icon{left:782px;top:10px}
  .account-links{left:832px;top:15px;display:flex;gap:10px;font:11px Arial, sans-serif;color:var(--white)}

  /* masthead */
  .masthead{left:0;top:36px;width:1019px;height:164px;background:var(--teal)}
  .brand{left:20px;top:62px;font:700 44px/1 var(--body);color:var(--white);letter-spacing:-.5px}
  .nav{left:286px;top:80px;display:flex;height:61px}
  .nav__item{font:300 26px/61px var(--heading);color:var(--white);padding:0 13px;text-transform:uppercase;white-space:nowrap}
  .nav__item--active{background:var(--ink);padding:0 18px}
  .nav__marker{left:317px;top:62px;width:0;height:0;border-left:13px solid transparent;border-right:13px solid transparent;border-top:13px solid var(--ink)}

  /* hero */
  .hero{left:15px;top:141px;width:990px;height:282px;background:var(--hero-edge)}
  .hero__stage{left:25px;top:149px;width:969px;height:265px;background:radial-gradient(ellipse at 30% 40%,#2f4a55 0%,#16262e 55%,#0d1519 100%)}
  .hero__title{left:43px;top:202px;font:300 32px/1 var(--heading);color:var(--teal-bright);letter-spacing:.3px}
  .hero__text{left:43px;top:252px;width:515px;font:12.5px/16px Arial, sans-serif;color:var(--white)}
  .hero__cta{left:42px;top:318px;width:152px;height:41px;background:var(--teal-bright);border-radius:3px;font:500 22px/41px var(--heading);color:var(--white);text-align:center}
  .hero__art{left:630px;top:156px;width:240px;height:340px;border-radius:16px;background:linear-gradient(160deg,#1d3c52 0%,#2a1a14 38%,#4a2a1c 70%,#23140d 100%);z-index:2}

  /* features */
  .feature{width:300px}
  .feature__icon{position:absolute;left:0;top:0}
  .feature__title{margin-left:71px;font:600 19px/1 var(--heading);color:var(--teal);text-transform:uppercase;letter-spacing:-.4px;white-space:nowrap}
  .feature__text{margin:8px 0 0 71px;font:12.5px/15px var(--body);color:var(--text-dark)}

  /* info panel */
  .info{left:15px;top:730px;width:988px;height:312px;background:var(--panel)}
  .info__frame{left:22px;top:737px;width:974px;height:298px;border:1px dashed #bdbdbd}
  .info__heading{left:39px;top:762px;font:300 32px/1 var(--body);color:var(--white)}
  .info__lead{left:41px;top:810px;width:545px;font:15px/18px var(--body);color:var(--text-light)}
  .info__lead span{color:var(--white)}
  .offer{width:260px}
  .offer__title{font:600 19px/1 var(--body);color:var(--teal-bright)}
  .offer__text{margin-top:7px;font:12.5px/15px var(--body);color:var(--text-light)}
  .offer__link{margin-top:3px;font:14px/1.2 var(--hand);color:var(--white)}
  .news{left:654px;top:765px;width:290px}
  .news__title{font:700 25px/1 var(--body);color:var(--white);margin-bottom:18px}
  .news__list{list-style:none}
  .news__item{position:relative;padding-left:24px;margin-bottom:10px;font:12.5px/15px var(--body);color:var(--text-light)}
  .news__item::before{content:"";position:absolute;left:3px;top:4px;border-left:6px solid var(--teal-bright);border-top:4px solid transparent;border-bottom:4px solid transparent}

  /* footer */
  .footer{left:0;top:1074px;width:1019px;height:53px;background:var(--teal)}
  .footer__nav{left:16px;top:1092px;display:flex;gap:17px;font:13px Arial, sans-serif;color:var(--white)}
  .footer__brand{left:870px;top:1086px;font:700 24px/1 var(--body);color:var(--white)}
  .legal{left:13px;top:1148px;font:11px/18px Arial, sans-serif;color:#111}
  .badges{left:755px;top:1143px;display:flex;gap:16px;align-items:center}
  .badge{height:36px;border-radius:3px}
  .badge--one{width:58px;background:#e9a23b}
  .badge--two{width:70px;background:#1d3f91}
  .badge--three{width:88px;background:#8a8a8a}
</style>
</head>
<body>

<div class="abs topbar"></div>
<div class="abs topbar__welcome">Welcome to pursedale</div>
<div class="abs account-tab"></div>
<svg class="abs account-tab__icon" width="28" height="22" viewBox="0 0 28 22" aria-hidden="true">
  <rect x="3" y="2" width="22" height="15" rx="2" fill="#eee"/>
  <rect x="6" y="5" width="16" height="9" fill="#555"/>
  <rect x="0" y="17" width="28" height="3" rx="1" fill="#eee"/>
</svg>
<div class="abs account-links"><span>sign up</span><span>sign in</span></div>

<header class="abs masthead"></header>
<div class="abs brand">Pursedale</div>
<div class="abs nav__marker"></div>
<nav class="abs nav">
  <span class="nav__item nav__item--active">Home</span>
  <span class="nav__item">Personal</span>
  <span class="nav__item">Business</span>
  <span class="nav__item">Guide</span>
  <span class="nav__item">Developers</span>
  <span class="nav__item">Support</span>
</nav>

<section>
  <div class="abs hero"></div>
  <div class="abs hero__stage" role="img" aria-label="Dark teal background of a glowing world map"></div>
  <h1 class="abs hero__title">PURCHASE. ANYWHERE. ANYTIME.</h1>
  <p class="abs hero__text">Ut wisi enim ad minim veniam, quis nostrud exerci tation ullamcorper suscipit lobortis nisl ut aliquip ex ea commodo consequat. Duis autem vel eum iriure dolor in hendrerit in vulputate velit esse molestie consequat, vel illum dolore eu feugiat nulla facilisis at vero eros.</p>
  <div class="abs hero__cta">SIGN UP NOW</div>
  <div class="abs hero__art" role="img" aria-label="Brown leather wallet holding a credit card"></div>
</section>

<section>
  <div class="abs feature" style="left:18px;top:518px">
    <svg class="feature__icon" width="52" height="48" viewBox="0 0 52 48" aria-hidden="true">
      <line x1="22" y1="2" x2="28" y2="16" stroke="#222" stroke-width="4" stroke-linecap="round"/>
      <rect x="0" y="16" width="50" height="6" fill="#00a6bf"/>
      <path d="M4 22h42l-4 20H8z" fill="#222"/>
      <g fill="#fff"><rect x="12" y="26" width="3" height="12"/><rect x="18" y="26" width="3" height="12"/><rect x="24" y="26" width="3" height="12"/><rect x="30" y="26" width="3" height="12"/><rect x="36" y="26" width="3" height="12"/></g>
    </svg>
    <h3 class="feature__title">Instant Transactions</h3>
    <p class="feature__text">Payments to others are instant; there is no waiting for clearing of funds.</p>
  </div>
  <div class="abs feature" style="left:362px;top:518px">
    <svg class="feature__icon" width="52" height="40" viewBox="0 0 52 40" aria-hidden="true">
      <rect x="1" y="5" width="50" height="34" rx="3" fill="#222"/>
      <rect x="1" y="11" width="50" height="6" fill="#fff"/>
      <rect x="6" y="20" width="14" height="5" fill="#00a6bf"/>
    </svg>
    <h3 class="feature__title">Multiple Wallets</h3>
    <p class="feature__text">Keep better track of your online funds with our wallet system.</p>
  </div>
  <div class="abs feature" style="left:703px;top:518px">
    <svg class="feature__icon" width="52" height="48" viewBox="0 0 52 48" aria-hidden="true">
      <path d="M17 10V4h18v6" fill="none" stroke="#222" stroke-width="4"/>
      <rect x="0" y="10" width="52" height="36" rx="3" fill="#00a6bf"/>
      <rect x="6" y="10" width="40" height="36" fill="#222"/>
      <path d="M6 10l20 14 20-14" fill="#fff"/>
    </svg>
    <h3 class="feature__title">Easy Deposit &amp; Withdraw</h3>
    <p class="feature__text">Simple transfers to and from your account, plus other flexible options.</p>
  </div>

  <div class="abs feature" style="left:18px;top:627px">
    <svg class="feature__icon" width="52" height="48" viewBox="0 0 52 48" aria-hidden="true">
      <path d="M15 20V12a11 11 0 0 1 22 0v8" fill="none" stroke="#00a6bf" stroke-width="5"/>
      <rect x="7" y="20" width="38" height="27" rx="3" fill="#222"/>
      <circle cx="26" cy="30" r="4" fill="#fff"/><rect x="24" y="31" width="4" height="9" fill="#fff"/>
    </svg>
    <h3 class="feature__title">Safe and Secured</h3>
    <p class="feature__text">The Vantoleaf website is built to protect your funds.</p>
  </div>
  <div class="abs feature" style="left:362px;top:627px">
    <svg class="feature__icon" width="58" height="48" viewBox="0 0 58 48" aria-hidden="true">
      <ellipse cx="15" cy="30" rx="14" ry="10" fill="#222"/><path d="M8 37l-3 9 9-6z" fill="#222"/>
      <ellipse cx="36" cy="16" rx="20" ry="14" fill="#00a6bf"/><path d="M42 28l6 10-13-7z" fill="#00a6bf"/>
    </svg>
    <h3 class="feature__title">24/7 Customer Support</h3>
    <p class="feature__text">PURSEDALE offers second to none customer support.</p>
  </div>
  <div class="abs feature" style="left:703px;top:627px">
    <svg class="feature__icon" width="52" height="48" viewBox="0 0 52 48" aria-hidden="true">
      <path d="M2 2v44h48" fill="none" stroke="#222" stroke-width="4"/>
      <path d="M8 38l12-14 9 8 17-18" fill="none" stroke="#00a6bf" stroke-width="4"/>
      <path d="M38 12h10v10z" fill="#00a6bf"/>
    </svg>
    <h3 class="feature__title">Residual Affiliate Income</h3>
    <p class="feature__text">PURSEDALE offers a simple yet extremely rewarding affiliate program.</p>
  </div>
</section>

<section>
  <div class="abs info"></div>
  <div class="abs info__frame"></div>
  <h2 class="abs info__heading">Welcome to Pursedale</h2>
  <p class="abs info__lead">Qrdelivane Transfer Technology is based on providing all its users with unique interfaces that allow to operate and control individual property rights for valuables (assets), stored at the specialized entities. <span>read more +</span></p>
  <div class="abs offer" style="left:40px;top:898px">
    <h3 class="offer__title">Shop Online</h3>
    <p class="offer__text">Purchase products and services online with ease and confidence. Your personal information is never shared.</p>
    <p class="offer__link">click here to sign up</p>
  </div>
  <div class="abs offer" style="left:321px;top:898px">
    <h3 class="offer__title">Sell Online</h3>
    <p class="offer__text">Accept payments from customers safely &amp; securely. Receive credit, debit card &amp; ewallet transfers instantly.</p>
    <p class="offer__link">click here to sign up</p>
  </div>
  <div class="abs news">
    <h2 class="news__title">LATEST NEWS</h2>
    <ul class="news__list">
      <li class="news__item">Pursedale Wishes You a Happy New Year!</li>
      <li class="news__item">Pursedale users in Turkey can top-up their QRZ purses via Korvel Telekom cash-in points</li>
      <li class="news__item">You can buy Glint Credits of Ternwick Online by paying with Qrdelivane</li>
      <li class="news__item">You can top-up your QRZ purse by using Pellacash vouchers in Turkey</li>
      <li class="news__item">Qrdelivane Voice protects your phone conversations</li>
    </ul>
  </div>
</section>

<footer>
  <div class="abs footer"></div>
  <nav class="abs footer__nav">
    <span>Home</span><span>Personal Accounts</span><span>Business Accounts</span><span>Guide</span><span>Developers</span><span>Contact Us</span>
  </nav>
  <div class="abs footer__brand">Pursedale</div>
  <div class="abs legal">Privacy Policy | FAQ | Terms of Use<br>COPYRIGHT © 2014. All Rights Reserved</div>
  <div class="abs badges">
    <div class="badge badge--one" role="img" aria-label="Card security badge"></div>
    <div class="badge badge--two" role="img" aria-label="Card verification badge"></div>
    <div class="badge badge--three" role="img" aria-label="Site security badge"></div>
  </div>
</footer>

</body>
</html>
```